LUMETTE INC. is a new Fashion Stylist, Design Merchandiser, and consultant in the fashion industry

We need a logo design for a new Calgary, Alberta based company that is in the business of making over your image, wardrobe and style for both business and personal purposes.

Target Market(s)

Professional female and male business people looking for a new style or complete fashion makeover including clothes closet merchandising and makeover.

Contact Information for Business Card

see the uploaded file

Number of Pages Required

1 page

Font styles to use
Script

Colors
fac994
fbe7d2
fee3d4

Requirements
Must have
• Fashion Industry theme that is very elegant and colorful using gold/bronze/silver color themes.
Nice to have
• Incorporate the company name with the creative font to come up with the appropriate "logo"

```html
<!DOCTYPE html>
<html lang="en">
<head>
<meta charset="utf-8">
<title>LUMETTE INC. – Business Card</title>
<link href="https://fonts.googleapis.com/css2?family=Great+Vibes&family=Poppins:wght@300;400&display=swap" rel="stylesheet">
<style>
  :root {
    --page-bg: #ffffff;
    --card-bg: #ffffff;
    --gold-light: #fac994;
    --gold-deep: #d9a865;
    --bronze: #a8773f;
    --champagne: #fbe7d2;
    --blush: #fee3d4;
    --band: rgba(158, 112, 62, 0.82);
    --ink: #4a4a4a;
    --white: #ffffff;
    --silver-light: #eef0f1;
    --silver-mid: #a7abb0;
    --silver-dark: #2b2c31;
  }
  * { margin: 0; padding: 0; box-sizing: border-box; }
  html, body {
    width: 1200px;
    height: 1000px;
    overflow: hidden;
    background: var(--page-bg);
    font-family: "Poppins", sans-serif;
  }
  .canvas { position: relative; width: 1200px; height: 1000px; }

  .card {
    position: absolute;
    top: 101px;
    width: 456px;
    height: 797px;
    background: var(--card-bg);
    box-shadow: 0 3px 8px rgba(0, 0, 0, 0.18);
    overflow: hidden;
  }
  .card--front { left: 120px; }
  .card--back { left: 625px; }

  .front-art { position: absolute; inset: 0; }
  .front-art .wordmark {
    font-family: "Poppins", sans-serif;
    font-weight: 300;
    font-size: 70px;
    fill: var(--white);
  }

  .holder { position: absolute; left: 108px; top: 528px; }
  .holder__name {
    font-family: "Great Vibes", cursive;
    font-size: 36px;
    font-weight: 400;
    color: var(--bronze);
    line-height: 1.1;
    white-space: nowrap;
  }
  .holder__role {
    font-size: 16px;
    font-weight: 300;
    color: var(--ink);
    margin-top: 2px;
  }

  .contact {
    position: absolute;
    left: 38px;
    top: 657px;
    display: grid;
    grid-template-columns: 70px auto;
    row-gap: 3px;
    font-size: 19px;
    font-weight: 300;
    line-height: 24px;
  }
  .contact__label { color: var(--bronze); }
  .contact__value { color: var(--ink); letter-spacing: 1.5px; }

  .back-illustration {
    position: absolute;
    inset: 0;
    background: linear-gradient(170deg, var(--white) 8%, var(--silver-light) 30%, var(--silver-mid) 60%, var(--silver-dark) 90%);
  }
  .back-band {
    position: absolute;
    left: 0;
    top: 337px;
    width: 100%;
    height: 118px;
    background: var(--band);
  }
  .back-band__name {
    position: absolute;
    left: 40px;
    top: 22px;
    font-size: 60px;
    font-weight: 300;
    color: var(--white);
    letter-spacing: 1px;
    white-space: nowrap;
  }
</style>
</head>
<body>
<main class="canvas">
  <section class="card card--front">
    <svg class="front-art" width="456" height="797" viewBox="0 0 456 797">
      <defs>
        <linearGradient id="gold-fill" x1="0" y1="0" x2="1" y2="1">
          <stop offset="0" stop-color="#e6b673"/>
          <stop offset="0.55" stop-color="#fac994"/>
          <stop offset="1" stop-color="#d9a865"/>
        </linearGradient>
      </defs>
      <polygon points="0,0 456,0 456,169 0,627" fill="url(#gold-fill)"/>
      <text class="wordmark" transform="translate(30,566) rotate(-45)" textLength="600" lengthAdjust="spacing">LUMETTE INC.</text>
    </svg>
    <div class="holder">
      <p class="holder__name">Marisol Van Dereck</p>
      <p class="holder__role">fashion stylist</p>
    </div>
    <div class="contact">
      <span class="contact__label">Tel:</span><span class="contact__value">403-555-0147</span>
      <span class="contact__label">Mail:</span><span class="contact__value">urname@email.com</span>
      <span class="contact__label">Web:</span><span class="contact__value">ursitename.com</span>
    </div>
  </section>

  <section class="card card--back">
    <div class="back-illustration" role="img" aria-label="Ink-wash fashion sketch of a woman in a wide-brimmed hat and a flowing dark gown"></div>
    <div class="back-band">
      <p class="back-band__name">LUMETTE INC.</p>
    </div>
  </section>
</main>
</body>
</html>
```